Carousel for Truck Parts Website

I need three images. 1400 x 1000. They all MUST be made in Adobe Illustrator -- Photoshop not accepted. It needs to be for Ridgeline Rig Supply. We'd like them to be patriotic themed (US flag). One with a announcement of towing/wrecker service 24/7. Call 6203417729. One with a shop online for heavy duty truck parts. Something like "Need Parts? Shop Online. Can't find your part, chat with us." Third would be "we have the one of the largest heavy truck salvage stores in the central United States." Need a part? Call 620-341-7729 and chat with us.

```html
<!DOCTYPE html>
<html lang="en">
<head>
<meta charset="utf-8">
<title>Ridgeline Rig Supply – Carousel Banners</title>
<link href="https://fonts.googleapis.com/css2?family=Anton&family=Oswald:wght@400;600&display=swap" rel="stylesheet">
<style>
  :root {
    --navy: #141c63;
    --navy-deep: #0f1650;
    --red: #e8141c;
    --white: #ffffff;
    --paper: #f4f4f5;
    --paper-shade: #e2e3e6;
    --stage: #b3b3b3;
    --ink: #2a2a2a;
    --flag-red: #b81d2c;
    --flag-blue: #1e2b6e;
    --headline: "Anton", "Oswald", sans-serif;
    --body: "Oswald", "Arial Narrow", sans-serif;
  }
  * { box-sizing: border-box; margin: 0; padding: 0; }
  html, body {
    width: 1200px; height: 1117px; overflow: hidden;
    background: var(--stage);
  }
  .carousel { position: relative; width: 1200px; height: 1117px; }
  .banner {
    position: absolute; width: 570px; height: 407px; overflow: hidden;
    background: linear-gradient(135deg, var(--white) 0%, var(--paper) 45%, var(--paper-shade) 100%);
    box-shadow: 0 10px 24px rgba(0,0,0,.25);
  }
  .banner--wrecker { left: 20px; top: 131px; }
  .banner--shop { left: 610px; top: 131px; }
  .banner--salvage { left: 315px; top: 578px; }

  .flag {
    position: absolute; right: 0; top: 0; width: 250px; height: 140px;
    background: linear-gradient(200deg, var(--flag-blue) 0%, var(--flag-blue) 30%, var(--flag-red) 55%, var(--white) 80%, rgba(255,255,255,0) 100%);
    clip-path: polygon(0 0, 100% 0, 100% 100%, 80% 85%, 55% 60%, 30% 40%, 12% 22%);
  }

  .brand { position: absolute; left: 44px; top: 30px; }
  .brand__name {
    font-family: var(--headline); font-size: 16px; color: var(--ink);
    letter-spacing: .3px;
  }
  .brand__tagline {
    font-family: var(--body); font-size: 6.5px; color: #555;
    text-transform: uppercase; margin-left: 40px; letter-spacing: .2px;
  }

  .headline {
    position: absolute; text-align: center; font-family: var(--headline);
    line-height: 1; text-transform: uppercase;
  }
  .headline .navy { color: var(--navy); }
  .headline .red { color: var(--red); }
  .headline__rule { flex: 1; height: 1.5px; background: var(--red); }

  .visual { position: absolute; border-radius: 8px; }

  .call-bar {
    position: absolute; left: 0; right: 0; bottom: 0; height: 85px;
    background: linear-gradient(180deg, #1a2380, var(--navy-deep));
    border-top: 4px solid var(--red);
    display: flex; align-items: center; padding-left: 34px; gap: 12px;
  }
  .call-bar__prompt {
    font-family: var(--headline); color: var(--white);
    font-size: 17px; line-height: 1.05; text-transform: uppercase;
  }
  .call-bar__icon { width: 24px; height: 34px; fill: var(--white); }
  .call-bar__number {
    font-family: var(--headline); color: var(--white);
    font-size: 50px; letter-spacing: .5px; line-height: 1; margin-left: -6px;
  }
</style>
</head>
<body>
<main class="carousel">

  <section class="banner banner--wrecker">
    <div class="flag" role="img" aria-label="Waving US flag"></div>
    <div class="brand">
      <div class="brand__name">Ridgeline Rig Supply</div>
      <div class="brand__tagline">Heavy-duty parts, towing and salvage under one roof</div>
    </div>
    <h2 class="headline" style="left:14px;top:104px;width:230px">
      <span class="navy" style="font-size:74px;display:block">24/7</span>
      <span class="red" style="font-size:44px;display:block;margin-top:4px">Wrecker</span>
      <span class="navy" style="font-size:48px;display:block;margin-top:2px">Service</span>
    </h2>
    <div class="visual" role="img" aria-label="Heavy-duty black tow truck with red wrecker boom"
         style="left:252px;top:110px;width:303px;height:200px;background:linear-gradient(120deg,#2a2a2e 0%,#121214 45%,#c41a20 70%,#e8e8ea 100%);opacity:.9"></div>
    <div class="call-bar">
      <div class="call-bar__prompt">Call now &amp;<br>chat with us</div>
      <svg class="call-bar__icon" viewBox="0 0 24 34" aria-hidden="true"><path d="M6 1c2 0 3 1 4 4l1 5c0 2-1 3-3 4 1 4 3 7 6 9 1-2 2-3 4-2l4 2c2 1 2 3 1 5-2 3-4 4-7 3C9 28 3 19 2 10 1 5 3 1 6 1z"/></svg>
      <div class="call-bar__number">620-341-7729.</div>
    </div>
  </section>

  <section class="banner banner--shop">
    <div class="flag" role="img" aria-label="Waving US flag"></div>
    <div class="brand">
      <div class="brand__name">Ridgeline Rig Supply</div>
      <div class="brand__tagline">Heavy-duty parts, towing and salvage under one roof</div>
    </div>
    <h2 class="headline" style="left:10px;top:118px;width:250px">
      <span class="navy" style="font-size:26px;display:block">Need Parts?</span>
      <span class="red" style="font-size:42px;display:block;margin-top:2px">Shop Online.</span>
      <span class="navy" style="font-size:21px;display:block;margin-top:4px">Can't find your part,</span>
      <span class="navy" style="font-size:21px;display:block;margin-top:2px">chat with us.</span>
    </h2>
    <div class="visual" role="img" aria-label="Truck parts: turbocharger, brake disc, brake pads, spark plugs and coil-over shock"
         style="left:270px;top:85px;width:295px;height:225px;background:linear-gradient(135deg,#d9dadd 0%,#9a9ca2 40%,#3a3b40 75%,#c41a20 100%);opacity:.85"></div>
    <div class="call-bar">
      <div class="call-bar__prompt">Call now &amp;<br>chat with us</div>
      <svg class="call-bar__icon" viewBox="0 0 24 34" aria-hidden="true"><path d="M6 1c2 0 3 1 4 4l1 5c0 2-1 3-3 4 1 4 3 7 6 9 1-2 2-3 4-2l4 2c2 1 2 3 1 5-2 3-4 4-7 3C9 28 3 19 2 10 1 5 3 1 6 1z"/></svg>
      <div class="call-bar__number">620-341-7729.</div>
    </div>
  </section>

  <section class="banner banner--salvage">
    <div class="flag" role="img" aria-label="Waving US flag"></div>
    <div class="brand">
      <div class="brand__name">Ridgeline Rig Supply</div>
      <div class="brand__tagline">Heavy-duty parts, towing and salvage under one roof</div>
    </div>
    <h2 class="headline" style="left:30px;top:112px;width:240px">
      <span class="navy" style="font-size:22px;display:block">One of the largest</span>
      <span class="red" style="font-size:32px;display:block;margin-top:3px">Heavy Truck</span>
      <span class="red" style="font-size:32px;display:block;margin-top:1px">Salvage Stores</span>
      <span class="navy" style="font-size:12px;display:flex;align-items:center;gap:6px;margin-top:3px">
        <span class="headline__rule"></span>in the<span class="headline__rule"></span>
      </span>
      <span class="navy" style="font-size:24px;display:block;margin-top:3px">Central United</span>
      <span class="navy" style="font-size:24px;display:block;margin-top:1px">States.</span>
    </h2>
    <div class="visual" role="img" aria-label="Grey heavy-duty semi truck cab"
         style="left:285px;top:95px;width:275px;height:215px;background:linear-gradient(120deg,#8e9096 0%,#54565c 40%,#1e1f22 70%,#d4d5d8 100%);opacity:.85"></div>
    <div class="call-bar">
      <div class="call-bar__prompt">Call now &amp;<br>chat with us</div>
      <svg class="call-bar__icon" viewBox="0 0 24 34" aria-hidden="true"><path d="M6 1c2 0 3 1 4 4l1 5c0 2-1 3-3 4 1 4 3 7 6 9 1-2 2-3 4-2l4 2c2 1 2 3 1 5-2 3-4 4-7 3C9 28 3 19 2 10 1 5 3 1 6 1z"/></svg>
      <div class="call-bar__number">620-341-7729.</div>
    </div>
  </section>

</main>
</body>
</html>
```